Australian IT Company requires Business Card Design

Bluepeak is an Australian company that specialises in IT consulting & support, software development, project management, network services.

We have been in business for 15 years.

* We require a business card with the following on it:
Logo
Address
Contact Details
Space for staff name, title & mobile number

Industry/Entity Type

Software

```html
<!DOCTYPE html>
<html lang="en">
<head>
<meta charset="utf-8">
<title>Bluepeak Business Card</title>
<link rel="stylesheet" href="https://fonts.googleapis.com/css2?family=Mulish:wght@400;600;800&display=swap">
<style>
  :root {
    --bg: #e9e6e1;
    --front-blue: #3c6892;
    --band: #37475a;
    --back-grey: #6c6c6e;
    --back-light: #7a7a7c;
    --mark-faint: #5d5d60;
    --accent-blue: #4f95dc;
    --text-light: #f2f2f2;
    --text-soft: #e4e4e4;
  }
  * { box-sizing: border-box; margin: 0; padding: 0; }
  html, body { width: 1200px; height: 750px; overflow: hidden; }
  body {
    background: var(--bg);
    font-family: "Mulish", "Century Gothic", sans-serif;
    position: relative;
  }
  .card {
    position: absolute;
    top: 224px;
    width: 532px;
    height: 304px;
    border-radius: 4px;
    overflow: hidden;
    box-shadow: 0 6px 18px rgba(0,0,0,0.18);
  }
  .card-front { left: 52px; background: var(--front-blue); }
  .card-back { left: 616px; background: var(--back-grey); }

  /* Front */
  .front-band {
    position: absolute;
    left: 60px; right: 0;
    top: 118px; height: 68px;
    background: var(--band);
    display: flex; align-items: center;
    padding-left: 34px; gap: 14px;
  }
  .brand-square {
    width: 30px; height: 30px;
    background: var(--text-light);
    flex: none;
  }
  .brand-text { color: var(--text-light); }
  .brand-name {
    font-weight: 600; font-size: 27px; letter-spacing: 1.5px;
    line-height: 1;
  }
  .brand-tagline {
    font-size: 7.5px; letter-spacing: 3.2px; text-transform: uppercase;
    margin-top: 4px; color: var(--text-soft);
  }

  /* Back */
  .back-diamond {
    position: absolute;
    left: 70px; top: 30px;
    width: 300px; height: 300px;
    background: var(--back-light);
    transform: rotate(45deg);
    opacity: 0.55;
  }
  .back-faint-square {
    position: absolute;
    right: 52px; top: 20px;
    width: 112px; height: 112px;
    background: var(--mark-faint);
  }
  .back-brand {
    position: absolute;
    left: 34px; top: 34px;
    display: flex; align-items: center; gap: 12px;
  }
  .back-brand .brand-square { width: 28px; height: 28px; }
  .back-brand .brand-name { font-size: 24px; }
  .back-brand .brand-tagline { font-size: 6.8px; letter-spacing: 2.9px; }

  .staff {
    position: absolute; left: 34px; top: 112px;
    color: var(--text-soft);
  }
  .staff-name { color: var(--accent-blue); font-size: 15px; font-weight: 600; }
  .staff-title { font-size: 12.5px; margin-top: 1px; }

  .contact-list {
    position: absolute; left: 34px; top: 158px;
    list-style: none; color: var(--text-soft);
    font-size: 12px; line-height: 17px;
  }
  .contact-list li { display: flex; align-items: center; gap: 8px; }
  .contact-list svg { width: 11px; height: 11px; fill: var(--accent-blue); flex: none; }

  .address {
    position: absolute; left: 60px; top: 218px;
    color: var(--text-light); font-weight: 800;
    font-size: 12.5px; line-height: 16px; font-style: normal;
  }
</style>
</head>
<body>
  <section class="card card-front" aria-label="Business card front">
    <div class="front-band">
      <span class="brand-square"></span>
      <div class="brand-text">
        <div class="brand-name">BLUEPEAK</div>
        <div class="brand-tagline">Smart solutions built to last</div>
      </div>
    </div>
  </section>

  <section class="card card-back" aria-label="Business card back">
    <div class="back-diamond"></div>
    <div class="back-faint-square"></div>

    <div class="back-brand">
      <span class="brand-square"></span>
      <div class="brand-text">
        <div class="brand-name">BLUEPEAK</div>
        <div class="brand-tagline">Smart solutions built to last</div>
      </div>
    </div>

    <div class="staff">
      <div class="staff-name">Daniel Hartley</div>
      <div class="staff-title">Managing Director</div>
    </div>

    <ul class="contact-list">
      <li>
        <svg viewBox="0 0 24 24" aria-hidden="true"><path d="M6.6 10.8a15.1 15.1 0 0 0 6.6 6.6l2.2-2.2a1 1 0 0 1 1-.25 11.4 11.4 0 0 0 3.6.57 1 1 0 0 1 1 1V20a1 1 0 0 1-1 1A17 17 0 0 1 3 4a1 1 0 0 1 1-1h3.5a1 1 0 0 1 1 1c0 1.25.2 2.45.57 3.57a1 1 0 0 1-.25 1z"/></svg>
        +61 3 9000 2480
      </li>
      <li>
        <svg viewBox="0 0 24 24" aria-hidden="true"><path d="M2 5h20v14H2z"/><path d="M3 6l9 7 9-7" fill="none" stroke="var(--back-grey)" stroke-width="1.6"/></svg>
        daniel@bluepeak.net.au
      </li>
      <li>
        <svg viewBox="0 0 24 24" aria-hidden="true"><circle cx="12" cy="12" r="10"/><path d="M2 12h20M12 2c3 3 3 17 0 20M12 2c-3 3-3 17 0 20" fill="none" stroke="var(--back-grey)" stroke-width="1.4"/></svg>
        www.bluepeak.net.au
      </li>
    </ul>

    <address class="address">
      14 Ridge Lane<br>
      Suite 3<br>
      Kingsford Vic 3032
    </address>
  </section>
</body>
</html>
```